Nutrivana, site for appointments between nutritionists and patients

Nutrivana is a platform for connecting nutritionists and patients with appointment scheduling and online payment.

We like teal, but we're not fixated on it.

The site must be simple, accessible and pleasant and dynamic and evoke the joy of nutrition while not forgetting the health aspect.

Example of illustration which tend towards what we are looking for.

Logo and graphic charter

Home page, simple little information

1)
Book a physical or video consultation with a dietitian (medirendo, you stay calm, lorée, vantoc)

2)
Reason for using Nutrivana

Access state-certified nutrition experts with several years of training (registration of professionals on the site only with adeli number and valid diploma)

Access the availability of tens of thousands of healthcare professionals.

Make an appointment online, 24/7, for a physical or video consultation.

Secure personal data

3)
You are a dietitian nutritionist

Use nutrivana to optimize your activity
Free up time by making an appointment online
Limit unfulfilled appointments with online payment
Take advantage of Nutrivana's notoriety to obtain better visibility
Use a commercial platform to develop your patient base
Use the platform's communication tools
Etc ...

Page 2 if applicable

List of professionals

Page 3 if search by specific name

Name photo
The essentials, map and access information, presentation, timetables, prices, site, make an appointment

Page 3 bis more in-depth presentation.

Page 4
agenda appointment booking page

Payment page

Professional page

Page 1
presentation of assets

Page 2 limited access

Rates with bronze, silver, gold, platinum account

Products, training and services page for sale

Blog page

Nutrivana is a platform that connects nutritionists and patients with online appointments and payment.

We like the teal color but we are not set on it.

The site must be simple, accessible, pleasant and dynamic and evoke the joy of nutrition while not forgetting the health aspect.

Example of illustrations that tend towards what we are looking for.

Our Logo is on the attachment

Home page

1)
Book a physical or video consultation with a dietician (ex site: medirendo, you stay calm, lorée, vantoc)

2)
Reasons to use Nutrivana

Access to experts in nutrition with several years of training (registration of professionals on the site only with adeli number and valid diploma)

Access the availability of tens of thousands of dieticians.

Secure personal data

3) You are a dietitian nutritionist

Free up time with online appointment booking
Limit the number of missed appointments thanks to online payment
Take advantage of Nutrivana's notoriety to get a better visibility
Use the communication tools of the platform
Etc ...

Page 2 if the patient don't choose a professional and put only a place.

List of professionals

Page 3 if searching by specific name

Photo name
The essentials, map and access information, presentation, opening hours, rates, site, make an appointment

Page 3 bis - more detailed presentation of dietician.

Page 4
diary page for making an appointment

Payment page

Blog page

Side Professional page

Page 1
presentation of assets

Page 2 (limited access)

Page 3

Products, training and services for sale page

Pour laisser le temps aux designers de travailler.

Target Market(s)

The general public

Number of Pages Required

5+ page

Colors
00AB8E
00BBA5
67D7C9
C6EFE9
E9F9F6

Requirements
Must have
• Read the project in the attached documents. Read the project on the attachments
Should not have
• No photographs

```html
<!DOCTYPE html>
<html lang="en">
<head>
<meta charset="utf-8">
<title>Nutrivana – Book a dietitian</title>
<link rel="stylesheet" href="https://fonts.googleapis.com/css2?family=Poppins:wght@400;500;600&display=swap">
<style>
:root{
  --green-deep:#0a8f55;
  --green-mid:#1fa566;
  --green-bright:#33b978;
  --teal:#56c2bc;
  --teal-soft:#67d7c9;
  --mint:#c6efe9;
  --mint-pale:#e9f9f6;
  --ink:#333c3a;
  --ink-soft:#7b8b89;
  --white:#ffffff;
}
*{box-sizing:border-box;margin:0;padding:0}
html,body{width:1200px;height:3716px;overflow:hidden}
body{font-family:"Poppins",sans-serif;background:var(--mint-pale);position:relative;color:var(--ink)}
.backdrop{position:absolute;left:0;top:0;width:1200px;height:3716px}
.abs{position:absolute}

/* header */
.brand{left:156px;top:40px;display:flex;align-items:center;gap:10px;font-weight:500;font-size:38px;color:var(--green-deep)}
.brand-dot{width:30px;height:30px;border-radius:50%;background:var(--green-deep)}
.nav{left:523px;top:116px;display:flex;gap:0}
.nav a{color:var(--white);text-decoration:none;font-size:15px;position:absolute;white-space:nowrap}
.btn-outline{left:959px;top:27px;width:169px;height:55px;border:3px solid var(--white);border-radius:28px;
  background:linear-gradient(90deg,var(--green-mid),var(--teal-soft));color:var(--white);font-size:18px;
  display:flex;align-items:center;justify-content:center;font-weight:500}

/* hero */
.hero-kicker{left:153px;top:305px;font-size:50px;font-weight:500;color:var(--green-deep)}
.hero-name{left:146px;top:360px;font-size:92px;font-weight:600;color:var(--green-bright);letter-spacing:-1px}
.btn-solid{left:151px;top:480px;width:163px;height:49px;border-radius:25px;border:3px solid var(--white);
  background:linear-gradient(90deg,var(--green-mid),var(--teal-soft));color:var(--white);font-size:18px;
  display:flex;align-items:center;justify-content:center;font-weight:500;box-shadow:0 4px 10px rgba(0,0,0,.12)}
.art{border-radius:40px}
.art-hero{left:591px;top:185px;width:419px;height:457px;background:linear-gradient(160deg,#1b7a4c,#7fd0b0 55%,#f2f7f5)}

/* consultation */
.art-plan{left:68px;top:995px;width:487px;height:394px;border-radius:160px 200px 200px 160px;background:linear-gradient(135deg,#e6eef6,#c9e3d6)}
.consult-title{left:613px;top:1010px;font-size:37px;line-height:42px;font-weight:500;color:var(--white)}
.pill{width:206px;height:69px;border-radius:35px;background:var(--white);color:var(--ink);font-size:21px;
  display:flex;align-items:center;justify-content:center;box-shadow:0 4px 12px rgba(0,0,0,.08)}

/* reasons */
.reason-title{left:149px;top:1592px;font-size:37px;line-height:43px;font-weight:500;color:var(--ink)}
.reason{left:149px;display:flex;gap:16px;align-items:center;width:440px}
.tick{flex:0 0 48px;height:48px;border-radius:50%;background:var(--teal-soft);display:flex;align-items:center;justify-content:center;box-shadow:0 3px 8px rgba(0,0,0,.1)}
.reason p{font-size:17px;line-height:20px;color:#4a5553}
.art-reasons{left:598px;top:1555px;width:582px;height:447px;background:linear-gradient(120deg,#e9f3ee,#9fd8a8 50%,#d9534f 95%)}

/* pro section */
.pro-title{left:0;width:1200px;top:2374px;text-align:center;font-size:37px;font-weight:500;color:var(--white)}
.card{width:249px;height:267px;background:var(--white);border-radius:46px 46px 46px 46px;
  display:flex;flex-direction:column;align-items:center;padding-top:24px}
.card svg{width:100px;height:100px}
.card p{margin-top:14px;font-size:17px;line-height:21px;color:var(--ink-soft);text-align:center;width:200px}

/* footer */
.foot-links{left:283px;top:3438px;list-style:none}
.foot-links li{font-size:19px;line-height:29px;color:var(--white)}
.foot-brand{left:450px;top:3420px;width:300px;display:flex;flex-direction:column;align-items:center;gap:18px}
.foot-brand .brand-dot{width:90px;height:90px;background:var(--white)}
.foot-brand span{font-size:52px;font-weight:500;color:var(--white)}
.contact{left:799px;display:flex;align-items:center;gap:26px;color:var(--white);font-size:19px;line-height:26px}
.contact-icon{width:50px;height:50px;border-radius:50%;border:2px solid var(--white);display:flex;align-items:center;justify-content:center}
.copyright{left:0;width:1200px;top:3670px;text-align:center;font-size:15px;color:var(--white)}
</style>
</head>
<body>

<svg class="backdrop" viewBox="0 0 1200 3716" aria-hidden="true">
  <defs>
    <linearGradient id="heroFill" x1="0" y1="0" x2="1" y2="1">
      <stop offset="0" stop-color="#0a8f55"/><stop offset="1" stop-color="#35bb78"/>
    </linearGradient>
    <linearGradient id="bandFill" gradientUnits="userSpaceOnUse" x1="0" y1="700" x2="0" y2="2150">
      <stop offset="0" stop-color="#0a8f55"/>
      <stop offset="0.28" stop-color="#2aa96c"/>
      <stop offset="0.6" stop-color="#bfe7dc"/>
      <stop offset="1" stop-color="#e6f6f3"/>
    </linearGradient>
    <linearGradient id="footFill" x1="0" y1="0" x2="1" y2="0">
      <stop offset="0" stop-color="#0a8f55"/><stop offset="1" stop-color="#3bb69a"/>
    </linearGradient>
  </defs>
  <path d="M397 0 C430 120 520 150 640 170 C760 190 820 300 880 420 C940 560 1050 680 1200 692 V0 Z" fill="url(#heroFill)"/>
  <path d="M0 800 C100 700 220 660 330 700 C450 740 560 800 700 780 C820 760 880 720 960 780 C1050 860 1080 980 1200 1000 V3716 H0 Z" fill="url(#bandFill)"/>
  <path d="M0 2180 C150 2240 300 2250 450 2240 C650 2225 750 2330 900 2320 C1050 2310 1120 2230 1200 2200 V3716 H0 Z" fill="#56c2bc"/>
  <path d="M0 3270 C150 3180 300 3160 450 3190 C650 3230 750 3290 900 3250 C1050 3210 1120 3200 1200 3240 V3716 H0 Z" fill="url(#footFill)"/>
</svg>

<!-- header -->
<div class="abs brand"><span class="brand-dot"></span>nutrivana</div>
<nav class="abs nav" style="left:0;top:0">
  <a style="left:523px;top:117px">Home</a>
  <a style="left:603px;top:117px">Professionals</a>
  <a style="left:741px;top:117px">Search</a>
  <a style="left:834px;top:117px">Appointment</a>
  <a style="left:971px;top:117px">Payment</a>
  <a style="left:1075px;top:117px">Blog</a>
</nav>
<div class="abs btn-outline">Book Now</div>

<!-- hero -->
<h1 class="abs hero-kicker">Welcome to</h1>
<div class="abs hero-name">nutrivana</div>
<div class="abs btn-solid">Book Now</div>
<div class="abs art art-hero" role="img" aria-label="Illustration of a woman leaning on a large smartphone showing the app and a green smoothie"></div>

<!-- consultation -->
<div class="abs art-plan" role="img" aria-label="Illustration of a diet plan on a phone with vegetables and a person using a laptop"></div>
<h2 class="abs consult-title">Book a physical<br>or video consultation<br>with a dietitian</h2>
<div class="abs pill" style="left:612px;top:1168px">Medirendo</div>
<div class="abs pill" style="left:837px;top:1168px">You stay calm</div>
<div class="abs pill" style="left:612px;top:1259px">Lorée</div>
<div class="abs pill" style="left:837px;top:1259px">Vantoc</div>

<!-- reasons -->
<h2 class="abs reason-title">Reason for<br>using Nutrivana</h2>
<div class="abs reason" style="top:1710px">
  <span class="tick"><svg width="24" height="24" viewBox="0 0 24 24"><path d="M5 12.5l4.5 4.5L19 7.5" fill="none" stroke="#fff" stroke-width="3.2" stroke-linecap="round" stroke-linejoin="round"/></svg></span>
  <p>Access state-certified nutrition experts with several years of training (registration of professionals on the site only with adeli number and valid diploma)</p>
</div>
<div class="abs reason" style="top:1819px">
  <span class="tick"><svg width="24" height="24" viewBox="0 0 24 24"><path d="M5 12.5l4.5 4.5L19 7.5" fill="none" stroke="#fff" stroke-width="3.2" stroke-linecap="round" stroke-linejoin="round"/></svg></span>
  <p>Access the availability of tens of thousands of healthcare professionals.</p>
</div>
<div class="abs reason" style="top:1903px">
  <span class="tick"><svg width="24" height="24" viewBox="0 0 24 24"><path d="M5 12.5l4.5 4.5L19 7.5" fill="none" stroke="#fff" stroke-width="3.2" stroke-linecap="round" stroke-linejoin="round"/></svg></span>
  <p>Make an appointment online, 24/7, for a physical or video consultation.</p>
</div>
<div class="abs reason" style="top:1974px">
  <span class="tick"><svg width="24" height="24" viewBox="0 0 24 24"><path d="M5 12.5l4.5 4.5L19 7.5" fill="none" stroke="#fff" stroke-width="3.2" stroke-linecap="round" stroke-linejoin="round"/></svg></span>
  <p>Secure personal data</p>
</div>
<div class="abs art art-reasons" role="img" aria-label="Illustration of a doctor in a phone with patients, broccoli, celery, asparagus and apples"></div>

<!-- professionals -->
<h2 class="abs pro-title">You are a dietitian nutritionist</h2>

<div class="abs card" style="left:182px;top:2492px">
  <svg viewBox="0 0 100 100"><circle cx="50" cy="52" r="36" fill="#22a76e"/></svg>
  <p>Use nutrivana to optimize your activity</p>
</div>
<div class="abs card" style="left:476px;top:2492px">
  <svg viewBox="0 0 100 100"><circle cx="50" cy="50" r="44" fill="#1ea86c"/><path d="M50 24v28l14 12" fill="none" stroke="#fff" stroke-width="6" stroke-linecap="round" stroke-linejoin="round"/></svg>
  <p>Free up time by making an appointment online</p>
</div>
<div class="abs card" style="left:769px;top:2492px">
  <svg viewBox="0 0 100 100"><rect x="28" y="12" width="62" height="38" rx="5" fill="#67d7c9" transform="rotate(-12 59 31)"/><rect x="12" y="34" width="68" height="50" rx="6" fill="#1ea86c"/><rect x="20" y="44" width="18" height="10" rx="2" fill="#fff"/><rect x="20" y="62" width="12" height="4" fill="#fff"/><rect x="36" y="62" width="12" height="4" fill="#fff"/><rect x="52" y="62" width="12" height="4" fill="#fff"/><rect x="20" y="72" width="26" height="4" fill="#fff"/></svg>
  <p>Limit unfulfilled appointments with online payment</p>
</div>
<div class="abs card" style="left:182px;top:2815px">
  <svg viewBox="0 0 100 100"><rect x="14" y="16" width="54" height="72" rx="4" fill="#1ea86c"/><rect x="30" y="10" width="22" height="12" rx="3" fill="#0a8f55"/><g fill="#fff"><rect x="22" y="32" width="8" height="6"/><rect x="34" y="33" width="24" height="4"/><rect x="22" y="46" width="8" height="6"/><rect x="34" y="47" width="24" height="4"/><rect x="22" y="60" width="8" height="6"/><rect x="34" y="61" width="18" height="4"/></g><circle cx="72" cy="70" r="17" fill="#2fb56f"/></svg>
  <p>Take advantage of Nutrivana's notoriety to obtain better visibility</p>
</div>
<div class="abs card" style="left:476px;top:2815px">
  <svg viewBox="0 0 100 100"><path d="M8 52 L50 14 L92 52" fill="none" stroke="#1ea86c" stroke-width="9" stroke-linejoin="round" stroke-linecap="round"/><path d="M22 48 V86 H78 V48 L50 24 Z" fill="#1ea86c"/><rect x="42" y="60" width="16" height="26" fill="#fff"/><rect x="66" y="20" width="10" height="20" fill="#1ea86c"/></svg>
  <p>Use a commercial platform to develop your patient base</p>
</div>
<div class="abs card" style="left:769px;top:2815px">
  <svg viewBox="0 0 100 100"><path d="M10 40h50v34H28l-14 12v-12h-4z" fill="#1ea86c"/><path d="M32 14h58v38h-6v12l-14-12H32z" fill="#67d7c9"/><g fill="#fff"><circle cx="50" cy="33" r="3"/><circle cx="61" cy="33" r="3"/><circle cx="72" cy="33" r="3"/></g></svg>
  <p>Use the platform's communication tools</p>
</div>

<!-- footer -->
<ul class="abs foot-links">
  <li>Home</li><li>Professionals</li><li>Search</li><li>Appointment</li><li>Payment</li><li>Blog</li>
</ul>
<div class="abs foot-brand"><span class="brand-dot"></span><span>nutrivana</span></div>

<div class="abs contact" style="top:3435px">
  <span class="contact-icon"><svg width="22" height="22" viewBox="0 0 24 24"><path d="M6.6 10.8a15 15 0 006.6 6.6l2.2-2.2c.3-.3.7-.4 1-.2 1.1.4 2.3.6 3.6.6.6 0 1 .4 1 1V20c0 .6-.4 1-1 1A17 17 0 013 4c0-.6.4-1 1-1h3.5c.6 0 1 .4 1 1 0 1.3.2 2.5.6 3.6.1.3 0 .7-.2 1z" fill="#fff"/></svg></span>
  <div>Phone<br>+00 4150 3362</div>
</div>
<div class="abs contact" style="top:3503px">
  <span class="contact-icon"><svg width="22" height="22" viewBox="0 0 24 24"><rect x="3" y="6" width="18" height="13" rx="2" fill="#fff"/><path d="M3.5 7l8.5 6 8.5-6" fill="none" stroke="#3bb69a" stroke-width="1.8"/></svg></span>
  <div>Email<br>hello@nutrivana-mail.com</div>
</div>
<div class="abs contact" style="top:3576px">
  <span class="contact-icon"><svg width="22" height="22" viewBox="0 0 24 24"><path d="M12 2a7 7 0 00-7 7c0 5 7 13 7 13s7-8 7-13a7 7 0 00-7-7z" fill="#fff"/><circle cx="12" cy="9" r="2.6" fill="#3bb69a"/></svg></span>
  <div>Verdane Street, 14<br>2600 Lindholt</div>
</div>

<div class="abs copyright">Copyright © 2022 All Right Reserved</div>

</body>
</html>
```